Healthy living company needs logo / business card

We are looking for a business identity for our company that operates in the Health and Wellness area.
Our audience is those open to hearing about the links between ill health and chemicals in the home as well as how to boost their health naturally through nutrition. We show people how to eliminate those toxins and share the message with others.
We also work with and mentor people who want to build their own business, share the message and create a leveraged income.
Our business name is: Brivora
The tag line we have is: Simple Changes ยท Healthy Living
Output for the project is:
Logo and business card design (2 people on the card).
Our perspective is for a modern, natural, simple, clean design (web 2.0 feel) that will appeal to a broad age range and audience. It should feel professional but not formal. It should not seem medical.
The logo should not be a gradient nor overly complex. Colouring should only be one or two colours at most. They can be bright, we are tending to lean towards green for obvious reasons but open to your thoughts.
Simplicity is the key.
The business card needs to be two sided. We like having the logo and card details on the front and then reversed out on the back with the logo and name in white on the colour block.
Please see the attached card brief document about the card content.

```html
<!DOCTYPE html>
<html lang="en">
<head>
<meta charset="utf-8">
<title>Brivora Business Card</title>
<link rel="stylesheet" href="https://fonts.googleapis.com/css2?family=Open+Sans:wght@400;600&display=swap">
<style>
  :root {
    --backdrop: #221e1c;
    --card: #ffffff;
    --ink: #1f1f1f;
    --ink-soft: #333333;
    --accent: #8cc63f;
    --divider: #c9e2a6;
  }
  * { margin: 0; padding: 0; box-sizing: border-box; }
  html, body {
    width: 1200px;
    height: 427px;
    overflow: hidden;
    background: var(--backdrop);
  }
  body {
    position: relative;
    font-family: "Open Sans", Arial, sans-serif;
    color: var(--ink);
  }
  .card {
    position: absolute;
    background: var(--card);
  }
  .card--front { left: 20px; top: 62px; width: 555px; height: 307px; }
  .card--back { left: 601px; top: 61px; width: 579px; height: 308px; }

  .contacts {
    position: absolute;
    left: 35px;
    top: 26px;
    font-size: 15px;
    line-height: 21px;
  }
  .contacts .person-name { font-weight: 600; }

  .office {
    position: absolute;
    right: 47px;
    top: 23px;
    text-align: right;
    font-size: 15px;
    line-height: 21.5px;
  }

  .brand {
    position: absolute;
    display: flex;
    align-items: center;
    gap: 14px;
  }
  .brand__name {
    font-weight: 400;
    color: var(--ink);
    line-height: 1;
    white-space: nowrap;
  }
  .brand__mark {
    flex: none;
    border-radius: 50%;
    background: var(--accent);
  }

  .card--front .brand { left: 262px; top: 200px; }
  .card--front .brand__name { font-size: 52px; }
  .card--front .brand__mark { width: 22px; height: 22px; }

  .card--back .brand { left: 38px; top: 128px; }
  .card--back .brand__name { font-size: 48px; }
  .card--back .brand__mark { width: 20px; height: 20px; }

  .divider {
    position: absolute;
    left: 292px;
    top: 39px;
    width: 1px;
    height: 221px;
    background: var(--divider);
  }

  .benefits {
    position: absolute;
    left: 322px;
    top: 36px;
    list-style: none;
    font-size: 16px;
    line-height: 22.8px;
    color: var(--ink-soft);
  }
</style>
</head>
<body>
  <section class="card card--front" aria-label="Card front">
    <div class="contacts">
      <p class="person-name">Name</p>
      <p>000000 000000</p>
      <p class="person-name">Name</p>
      <p>Cell : 000000 000000</p>
    </div>
    <div class="office">
      <p>Off. Phone : 000000000</p>
      <p>hello@livebrivora.com</p>
    </div>
    <div class="brand">
      <span class="brand__name">Brivora</span>
      <span class="brand__mark"></span>
    </div>
  </section>

  <section class="card card--back" aria-label="Card back">
    <div class="brand">
      <span class="brand__name">Brivora</span>
      <span class="brand__mark"></span>
    </div>
    <div class="divider"></div>
    <ul class="benefits">
      <li>Multiple Streams of Income</li>
      <li>Financial Freedom</li>
      <li>Own my Own Business</li>
      <li>More Time</li>
      <li>Personal Development</li>
      <li>Health and Vitality</li>
      <li>Help Others</li>
      <li>Meet New People</li>
      <li>Retirement Plan</li>
      <li>Leave a Legacy</li>
    </ul>
  </section>
</body>
</html>
```